Odvetnik - Attorney at law
Sodni tolmač za angleški jezik - English language Court Interpreter
Simple
Marjan Lesk
Odvetnik - Attorney at law Sodni tolmač za angleški jezik - English Language Court Interpreter
Brinjeva ulica 41 6000 Koper Slovenija
info@marjanlesk.example
www.marjanlesk.example
I invite all designers under logo project Attorney Marjan Lesk to participate. Please inform all designers.

```html
<!DOCTYPE html>
<html lang="sl">
<head>
<meta charset="utf-8">
<title>Marjan Lesk – Business Card</title>
<link href="https://fonts.googleapis.com/css2?family=Marcellus&family=Arimo:wght@400;700&display=swap" rel="stylesheet">
<style>
  :root {
    --bg: #e9e9ee;
    --navy-dark: #262670;
    --navy-light: #3d3d9c;
    --ink: #2b2b72;
    --white: #ffffff;
    --orange: #f07a22;
    --muted-light: #d7d8ef;
    --muted-dark: #4b4b7e;
  }
  * { box-sizing: border-box; margin: 0; padding: 0; }
  html, body { width: 1200px; height: 1052px; overflow: hidden; }
  body {
    background: var(--bg);
    display: flex;
    flex-direction: column;
    align-items: center;
    justify-content: center;
    gap: 40px;
    font-family: "Arimo", Arial, sans-serif;
  }
  .card {
    position: relative;
    width: 760px;
    height: 466px;
    border-radius: 24px;
    overflow: hidden;
    box-shadow: 0 6px 18px rgba(0,0,0,0.18);
  }
  .card--dark {
    background: linear-gradient(135deg, var(--navy-dark) 0%, var(--navy-light) 100%);
    color: var(--white);
  }
  .card--light {
    background: var(--white);
    color: var(--ink);
  }
  .brand {
    position: absolute;
    left: 56px;
    top: 52px;
    display: flex;
    align-items: center;
    gap: 18px;
  }
  .brand__dot {
    width: 58px;
    height: 58px;
    border-radius: 50%;
    background: var(--orange);
    flex: none;
  }
  .brand__name {
    font-family: "Marcellus", Georgia, serif;
    font-size: 60px;
    letter-spacing: 2px;
    line-height: 1;
    text-transform: uppercase;
  }
  .brand__role {
    font-family: "Marcellus", Georgia, serif;
    font-size: 25px;
    margin-top: 6px;
  }
  .contact {
    position: absolute;
    left: 120px;
    right: 40px;
    top: 232px;
    text-align: center;
    font-size: 23px;
    line-height: 1.3;
  }
  .contact__line span + span { margin-left: 14px; }
  .contact__web { color: var(--orange); }
  .contact__web span + span { margin-left: 22px; }
  .service {
    position: absolute;
    left: 0;
    right: 0;
    bottom: 0;
    height: 72px;
    display: flex;
    align-items: center;
    justify-content: center;
    font-size: 18px;
    letter-spacing: 0.6px;
    text-transform: uppercase;
  }
  .card--dark .service { background: rgba(255,255,255,0.06); color: var(--muted-light); }
  .card--light .service { color: var(--muted-dark); }
</style>
</head>
<body>

<section class="card card--dark">
  <div class="brand">
    <span class="brand__dot"></span>
    <div>
      <div class="brand__name">Marjan Lesk</div>
      <div class="brand__role">Odvetnik - Attorney at law</div>
    </div>
  </div>
  <div class="contact">
    <p class="contact__line">Brinjeva ulica 41, 6000 Koper, Slovenija</p>
    <p class="contact__line"><span>Ph. +386 5 6112040</span><span>Cell +386 41550318</span><span>Fax +386 5 6112041</span></p>
    <p class="contact__web"><span>info@marjanlesk.example</span><span>www.marjanlesk.example</span></p>
  </div>
  <p class="service">Sodni tolmač za angleški jezik • English language court interpreter</p>
</section>

<section class="card card--light">
  <div class="brand">
    <span class="brand__dot"></span>
    <div>
      <div class="brand__name">Marjan Lesk</div>
      <div class="brand__role">Odvetnik - Attorney at law</div>
    </div>
  </div>
  <div class="contact">
    <p class="contact__line">Brinjeva ulica 41, 6000 Koper, Slovenija</p>
    <p class="contact__line"><span>Ph. +386 5 6112040</span><span>Cell +386 41550318</span><span>Fax +386 5 6112041</span></p>
    <p class="contact__web"><span>info@marjanlesk.example</span><span>www.marjanlesk.example</span></p>
  </div>
  <p class="service">Sodni tolmač za angleški jezik • English language court interpreter</p>
</section>

</body>
</html>
```